Geschäftspapiere für Filmproduktion
Zielgruppe
KLUVE Film produziert professionell hochwertige Filme für Unternehmen, Dienstleister, Kommunen und Veranstalter. Egal ob Sie informieren, werben, dokumentieren, schulen oder ein Event festhalten möchten: Wir entwickeln für jedes Budget ein abgestimmtes Konzept und helfen Ihnen durch die Faszination von bewegten eindrucksvollen Bildern Ihre Zielgruppe erfolgreich und optimal zu erreichen.
Aufgabenstellung
Benötigt wird ein modernes Briefpapier / ein Rechnungspapier für den Druck (WICHTIG: Auf dem Papier werden später per Software die Rechnungspositionen eingedruckt) - das Rechnungspapier sollte folgende Elemente enhalten: Logo / Slogan (Filme die begeistern), Kontaktdaten (Adresse, Telefon, Fax, E-Mail, Web) Datum, Rechnungsnummer, Lieferdatum, Bankverbindung, Umsatzsteuer-ID) Viele Daten sind auf www.kluve-film-beispiel.de unter Impressum einzusehen.

```html
<!DOCTYPE html>
<html lang="de">
<head>
<meta charset="utf-8">
<title>Kluve Film – Geschäftsausstattung</title>
<link href="https://fonts.googleapis.com/css2?family=Questrial&family=Michroma&display=swap" rel="stylesheet">
<style>
:root{
  --blue:#1b87c9;
  --grey:#8a8a8a;
  --grey-light:#c9c9c9;
  --ink:#3c3c3c;
  --paper:#ffffff;
  --bg:#f1f1f1;
}
*{margin:0;padding:0;box-sizing:border-box}
html,body{width:1200px;height:402px;overflow:hidden;background:var(--bg)}
body{position:relative;font-family:"Questrial",sans-serif;color:var(--ink)}
.sheet{position:absolute;background:var(--paper);box-shadow:0 1px 3px rgba(0,0,0,.18)}
.letter{top:14px;width:263px;height:372px}
.letter-1{left:11px}.letter-2{left:291px}.letter-3{left:568px}

.brand{position:absolute;white-space:nowrap;font-size:11px;line-height:1;color:var(--grey)}
.letter .brand{top:20px;right:22px}

.sender-line{position:absolute;top:56px;left:31px;font-size:2.6px;color:var(--ink);white-space:nowrap}
.fold{position:absolute;left:0;width:9px;height:.6px}
.fold.blue{top:127px;background:var(--blue)}
.fold.grey{top:135px;background:var(--grey)}

.small{font-size:3.3px;line-height:4.6px;position:absolute;white-space:nowrap}
.small strong{color:#000;font-weight:normal}

.band-grey{position:absolute;left:0;right:0;bottom:0;height:8px;background:var(--grey-light)}
.band-blue{position:absolute;right:0;bottom:0;width:76px;height:8px;background:var(--blue);color:#fff;font-size:3.3px;line-height:8px;padding-left:9px;white-space:nowrap}
.line-grey{position:absolute;left:0;right:0;bottom:0;height:2px;background:var(--grey-light)}
.line-blue{position:absolute;right:0;bottom:0;width:75px;height:2px;background:var(--blue)}
.bar-side{position:absolute;left:0;bottom:0;width:2px;height:39px;background:var(--blue)}
.ico{display:inline-block;width:2.6px;height:2.6px;background:var(--blue);border-radius:50%;margin-right:2px;vertical-align:middle}

.envelope-long{left:632px;top:150px;width:262px;height:124px}
.envelope-long .brand{top:20px;right:18px}
.envelope-long .sender-line{top:58px;left:36px}
.envelope-long .recipient{position:absolute;top:68px;left:36px;font-size:3.8px;line-height:5px}

.card{width:108px;height:70px}
.card-1{left:938px;top:30px}
.card-2{left:1057px;top:30px;background:var(--blue);color:#fff}
.card-3{left:938px;top:124px}
.card-4{left:1057px;top:124px}
.card .brand.big{left:16px;top:30px;font-size:15px}
.card-3 .brand.big{top:24px}
.person{font-family:"Michroma",sans-serif;font-size:4.6px;letter-spacing:.4px;white-space:nowrap}
.role{font-size:3.2px;font-style:italic;display:block;font-family:"Questrial",sans-serif;letter-spacing:0}
.card-2 .person{position:absolute;left:10px;top:11px}
.card-2 .small{left:10px;top:31px;color:#fff}
.card-2 .ico{background:#fff}
.card-3 .url{position:absolute;left:0;right:0;bottom:0;height:7px;background:var(--blue);color:#fff;font-size:4px;line-height:7px;text-align:center}
.card-4 .brand{left:8px;top:9px;font-size:8px}
.card-4 .addr{left:68px;top:9px}
.card-4 .person{position:absolute;left:10px;top:33px;color:var(--ink)}
.card-4 .contact{left:10px;top:49px;line-height:4px}
.card-4 .contact span{display:inline-block;width:18px}

.envelope-c{left:918px;top:258px;width:268px;height:132px;border:.6px solid #555}
.flap{position:absolute;left:918px;top:234px;width:268px;height:24px}
.flap-text{position:absolute;left:0;right:0;top:4px;text-align:center;color:#fff;font-size:3.8px;line-height:5px;transform:rotate(180deg)}
.envelope-c .stripe{position:absolute;left:0;top:60px;width:2px;height:55px;background:var(--blue)}
.envelope-c .brand{left:30px;top:42px}
.envelope-c .window{position:absolute;left:26px;top:61px;width:104px;height:52px;border:.6px solid #333;border-radius:4px}
.envelope-c .window .sender-line{top:5px;left:6px}
.envelope-c .window .recipient{position:absolute;top:15px;left:11px;font-size:3.6px;line-height:5px}
</style>
</head>
<body>

<section class="sheet letter letter-1">
  <p class="brand">Kluve Film</p>
  <p class="sender-line">KLUVE Film &nbsp;|&nbsp; Birkenweg 7 &nbsp;|&nbsp; 34410 Talheim</p>
  <span class="fold blue"></span><span class="fold grey"></span>
  <div class="small" style="left:31px;top:340px">Bankverbindung</div>
  <div class="small" style="left:75px;top:340px">Musterbank Talheim<br>IBAN &nbsp;&nbsp;&nbsp;&nbsp;1234 56789012 3456789012<br>BIC &nbsp;&nbsp;&nbsp;&nbsp;&nbsp;&nbsp;GENODEX1ABC<br><span style="line-height:7px">USt-IdNr. &nbsp;DE123456789</span></div>
  <div class="small" style="left:196px;top:324px"><strong>KLUVE Film<br>Jonas Albrecht</strong><br><span style="display:block;margin-top:2px">Birkenweg 7<br>34410 Talheim</span><span style="display:block;margin-top:2px">Telefon: &nbsp;&nbsp;0 12 34 &nbsp;567 890 1<br>Telefax: &nbsp;&nbsp;0 12 34 &nbsp;567 890 2<br>Email: &nbsp;&nbsp;&nbsp;&nbsp;kontakt@kluve-film-beispiel.de</span></div>
  <div class="band-grey"></div>
  <div class="band-blue">Web: &nbsp;&nbsp;&nbsp;www.kluve-film-beispiel.de</div>
</section>

<section class="sheet letter letter-2">
  <p class="brand">Kluve Film</p>
  <p class="sender-line">KLUVE Film &nbsp;|&nbsp; Birkenweg 7 &nbsp;|&nbsp; 34410 Talheim</p>
  <span class="fold blue"></span><span class="fold grey"></span>
  <div class="small" style="left:31px;top:341px"><strong>KLUVE Film &nbsp;·&nbsp; Jonas Albrecht</strong><br><span style="display:block;margin-top:2px">Birkenweg 7<br>34410 Talheim<br><br>USt-IdNr. &nbsp;DE123456789</span></div>
  <div class="small" style="left:92px;top:348px">Bankverbindung:<br>Musterbank Talheim<br>IBAN &nbsp;1234 56789012 3456789012<br>BIC &nbsp;&nbsp;GENODEX1ABC</div>
  <div class="small" style="left:199px;top:348px"><i class="ico"></i>0 12 34 &nbsp;567 890 1<br><i class="ico"></i>0 12 34 &nbsp;567 890 2<br><i class="ico"></i>kontakt@kluve-film-beispiel.de<br><i class="ico"></i>www.kluve-film-beispiel.de</div>
  <div class="line-grey"></div><div class="line-blue"></div>
</section>

<section class="sheet letter letter-3">
  <p class="brand">Kluve Film</p>
  <p class="sender-line">KLUVE Film &nbsp;|&nbsp; Birkenweg 7 &nbsp;|&nbsp; 34410 Talheim</p>
  <span class="fold blue"></span><span class="fold grey"></span>
  <div class="small" style="left:31px;top:341px"><strong>KLUVE Film &nbsp;·&nbsp; Jonas Albrecht</strong><br><span style="display:block;margin-top:2px">Birkenweg 7<br>34410 Talheim<br><br>USt-IdNr. &nbsp;DE123456789</span></div>
  <div class="small" style="left:92px;top:348px">Bankverbindung:<br>Musterbank Talheim<br>IBAN &nbsp;1234 56789012 3456789012<br>BIC &nbsp;&nbsp;GENODEX1ABC</div>
  <div class="small" style="left:199px;top:348px"><i class="ico"></i>0 12 34 &nbsp;567 890 1<br><i class="ico"></i>0 12 34 &nbsp;567 890 2<br><i class="ico"></i>kontakt@kluve-film-beispiel.de<br><i class="ico"></i>www.kluve-film-beispiel.de</div>
  <div class="bar-side"></div>
</section>

<section class="sheet envelope-long">
  <p class="brand">Kluve Film</p>
  <p class="sender-line">KLUVE Film &nbsp;|&nbsp; Birkenweg 7 &nbsp;|&nbsp; 34410 Talheim</p>
  <p class="recipient">Firma<br>Beispiel 1-2-3 GmbH<br>Herrn Dr. Weber<br>Schulhausstrasse 23<br><span style="display:block;margin-top:2px">88340 Irgendwo</span></p>
</section>

<section class="sheet card card-1">
  <p class="brand big">Kluve Film</p>
</section>
<section class="sheet card card-2">
  <p class="person">JONAS ALBRECHT<span class="role">Position Bezeichnung</span></p>
  <div class="small">Birkenweg 7 &nbsp;·&nbsp; 34410 Talheim<br><span style="display:block;margin-top:3px"><i class="ico"></i>0 12 34 &nbsp;567 890 1<br><i class="ico"></i>0 12 34 &nbsp;567 890 2<br><i class="ico"></i>0 170 &nbsp;&nbsp;12 34 567<br><i class="ico"></i>j.albrecht@kluve-film-beispiel.de<br><i class="ico"></i>www.kluve-film-beispiel.de</span></div>
</section>
<section class="sheet card card-3">
  <p class="brand big">Kluve Film</p>
  <div class="url">www.kluve-film-beispiel.de</div>
</section>
<section class="sheet card card-4">
  <p class="brand">Kluve Film</p>
  <div class="small addr">Birkenweg 7<br>34410 Talheim</div>
  <p class="person">JONAS ALBRECHT<span class="role">Position Bezeichnung</span></p>
  <div class="small contact"><span>Telefon:</span>0 12 34 &nbsp;567 890 1<br><span>Telefax:</span>0 12 34 &nbsp;567 890 2<br><span>Mobil:</span>0 170 &nbsp;12 34 567<br><span>Email:</span>j.albrecht@kluve-film-beispiel.de</div>
</section>

<svg class="flap" viewBox="0 0 268 24" aria-hidden="true"><polygon points="0,24 20,0 248,0 268,24" fill="var(--blue)"/></svg>
<div class="flap"><p class="flap-text">KLUVE Film &nbsp;·&nbsp; Jonas Albrecht<br>Birkenweg 7 &nbsp;·&nbsp; 34410 Talheim</p></div>
<section class="sheet envelope-c">
  <div class="stripe"></div>
  <p class="brand">Kluve Film</p>
  <div class="window">
    <p class="sender-line">KLUVE Film &nbsp;|&nbsp; Birkenweg 7 &nbsp;|&nbsp; 34410 Talheim</p>
    <p class="recipient">Firma<br>Beispiel 1-2-3 GmbH<br>Herrn Dr. Weber<br>Schulhausstrasse 23<br><span style="display:block;margin-top:2px">88340 Irgendwo</span></p>
  </div>
</section>

</body>
</html>
```